Skincare company needing leaflet/flyer for selling products

Hi guys. I am needing a leaflet/flyer design for my new skincare business - Brenna skincare. Our products are all made in Australia from natural ingredients. The leaflet should specify that all products have - organic ingredients, cruelty free, no nasty chemicals or ingredients and a made in Australia logo.
The pictures I have supplied, if they can be made more professional looking for the design without any background that would be great. It should look like other competitors and very appealing. The leaflet can be double sided so it looks more easy to read
The information is provided as follows:
Product, skin types the product is for, ml capacity of bottle, key ingredients and price.
Contact is a whatsapp number and website will be up later so if a leaflet can be made with and without the website.
This leaflet/flyer can be easy to read, not hard on the eyes and easy to understand. Focus on blue shades and other calm colours to make it easy on the eyes and attractive to see. Thank you guys for helping
Updates
Getting professional product photos done that can be updated on the leaflet/flyers once received. More submissions are welcomed
Target Market(s)
People wanting good quality skincare that does not contain harmful chemicals and is organic
Look and feel

```html
<!DOCTYPE html>
<html lang="en">
<head>
<meta charset="utf-8">
<title>Brenna Skincare – Product Leaflet</title>
<link href="https://fonts.googleapis.com/css2?family=Cinzel:wght@400&family=Crimson+Pro:ital,wght@0,400;0,600;0,700;1,600&display=swap" rel="stylesheet">
<style>
  :root {
    --navy: #141a2e;
    --white: #ffffff;
    --stage: #ececee;
    --ink: #141a2e;
    --ink-soft: #2b3148;
  }
  * { margin: 0; padding: 0; box-sizing: border-box; }
  html, body { width: 1200px; height: 2280px; overflow: hidden; background: var(--stage); }
  body { position: relative; font-family: "Crimson Pro", Georgia, serif; color: var(--ink); }

  .page { position: absolute; left: 232px; width: 737px; height: 1040px; background: var(--white); overflow: hidden; box-shadow: 0 2px 10px rgba(0,0,0,.12); }
  .page--front { top: 79px; }
  .page--back { top: 1165px; }
  .page svg.shapes { position: absolute; inset: 0; }

  /* Front */
  .brand-mark { position: absolute; left: 294px; top: 82px; width: 150px; height: 150px; background: var(--navy); }
  .brand-name { position: absolute; left: 0; right: 0; text-align: center; font-family: "Cinzel", Georgia, serif; font-weight: 400; color: var(--navy); }
  .brand-name--main { top: 278px; font-size: 96px; letter-spacing: 0.12em; line-height: 1; padding-left: .12em; }
  .brand-name--sub { top: 402px; font-size: 30px; letter-spacing: 0.32em; line-height: 1; padding-left: .32em; }

  .promise { position: absolute; top: 704px; width: 150px; text-align: center; color: var(--white); }
  .promise svg { display: block; margin: 0 auto; }
  .promise__label { margin-top: 12px; font-size: 14px; line-height: 17px; text-transform: uppercase; letter-spacing: .02em; }
  .promise--organic { left: 129px; }
  .promise--cruelty { left: 291px; }
  .promise--chemical { left: 456px; }

  .front-contact { position: absolute; left: 0; right: 0; top: 904px; text-align: center; color: var(--white); }
  .front-contact__icons { display: flex; justify-content: center; gap: 14px; margin-bottom: 18px; }
  .front-contact p { font-size: 17px; line-height: 21px; }

  /* Back */
  .product { position: absolute; width: 310px; }
  .product--light { color: var(--ink); }
  .product--dark { color: var(--white); }
  .product__name { font-style: italic; font-weight: 600; font-size: 24px; line-height: 28px; }
  .product__meta { margin-top: 6px; font-size: 10px; line-height: 12px; }
  .product__price { font-size: 14px; font-weight: 700; }
  .product__skin { font-size: 10px; line-height: 12px; }
  .product__key { margin-top: 14px; font-style: italic; font-weight: 600; font-size: 13px; line-height: 16px; }
  .ingredients { list-style: none; margin-top: 12px; }
  .ingredients li { font-size: 10px; line-height: 11.5px; margin-bottom: 1px; }
  .ingredients strong { display: block; font-weight: 700; text-transform: uppercase; position: relative; padding-left: 8px; }
  .ingredients strong::before { content: ""; position: absolute; left: 0; top: 3px; width: 5px; height: 5px; border-top: 1px solid currentColor; border-bottom: 1px solid currentColor; box-shadow: inset 0 -2px 0 -1px currentColor; }
  .ingredients span { display: block; padding-left: 18px; }

  .col-left { left: 41px; }
  .col-right { left: 389px; }
  .row-1 { top: 44px; }
  .row-2 { top: 280px; }
  .row-3 { top: 558px; }
  .row-4 { top: 788px; }
  .product--body { width: 340px; }
  .product--body .product__key { margin-top: 22px; }

  .divider { position: absolute; left: 368px; width: 1px; background: var(--ink-soft); }
  .divider--top { top: 40px; height: 190px; }
  .divider--bottom { top: 556px; height: 222px; }

  .contact-card { position: absolute; left: 526px; top: 872px; color: var(--white); }
  .contact-card h3 { font-weight: 600; font-size: 16px; line-height: 20px; }
  .contact-card p { font-size: 12px; line-height: 15px; }
  .contact-card .company { margin: 9px 0 14px; }
  .contact-card .line { display: flex; align-items: center; gap: 8px; }
</style>
</head>
<body>

<section class="page page--front">
  <svg class="shapes" width="737" height="1040" viewBox="0 0 737 1040" aria-hidden="true">
    <path d="M0 572 C110 545 190 600 320 615 C450 630 520 545 737 528" fill="none" stroke="var(--navy)" stroke-width="5"/>
    <path d="M0 600 C110 580 190 630 320 645 C450 660 540 575 737 558 L737 1040 L0 1040 Z" fill="var(--navy)"/>
  </svg>

  <div class="brand-mark"></div>
  <div class="brand-name brand-name--main">BRENNA</div>
  <div class="brand-name brand-name--sub">SKINCARE</div>

  <div class="promise promise--organic">
    <svg width="110" height="110" viewBox="0 0 110 110" aria-hidden="true">
      <circle cx="55" cy="55" r="52" fill="none" stroke="#fff" stroke-width="1.4" stroke-dasharray="250 77"/>
      <circle cx="55" cy="55" r="44" fill="#fff"/>
      <path d="M55 68 L40 52 A8 8 0 0 1 55 42 A8 8 0 0 1 70 52 Z" fill="var(--navy)"/>
      <path d="M44 74 Q55 66 66 74" fill="none" stroke="var(--navy)" stroke-width="2"/>
    </svg>
    <p class="promise__label">% 100<br>Organic</p>
  </div>

  <div class="promise promise--cruelty">
    <svg width="110" height="110" viewBox="0 0 110 110" aria-hidden="true">
      <circle cx="55" cy="55" r="52" fill="none" stroke="#fff" stroke-width="1.4" stroke-dasharray="250 77"/>
      <circle cx="55" cy="55" r="44" fill="#fff"/>
      <path d="M55 74 C44 62 46 44 55 34 C64 44 66 62 55 74 Z" fill="var(--navy)"/>
      <path d="M53 75 C40 74 33 64 32 54 C44 55 52 62 53 75 Z" fill="var(--navy)"/>
      <path d="M57 75 C70 74 77 64 78 54 C66 55 58 62 57 75 Z" fill="var(--navy)"/>
      <path d="M55 74 V40" stroke="#fff" stroke-width="1.2"/>
    </svg>
    <p class="promise__label">Cruelty<br>Free</p>
  </div>

  <div class="promise promise--chemical">
    <svg width="110" height="110" viewBox="0 0 110 110" aria-hidden="true">
      <circle cx="55" cy="55" r="52" fill="none" stroke="#fff" stroke-width="1.4" stroke-dasharray="250 77"/>
      <circle cx="55" cy="55" r="44" fill="#fff"/>
      <rect x="50" y="30" width="10" height="16" fill="var(--navy)"/>
      <rect x="47" y="28" width="16" height="4" fill="var(--navy)"/>
      <circle cx="55" cy="60" r="17" fill="var(--navy)"/>
      <circle cx="50" cy="62" r="3" fill="#fff"/>
      <circle cx="60" cy="62" r="3" fill="#fff"/>
    </svg>
    <p class="promise__label">Chemicals<br>Free</p>
  </div>

  <div class="front-contact">
    <div class="front-contact__icons">
      <svg width="22" height="22" viewBox="0 0 24 24" aria-hidden="true"><path d="M6 3 L9 3 L10.5 8 L8.5 9.5 C9.5 12 12 14.5 14.5 15.5 L16 13.5 L21 15 L21 18 C21 19.5 20 21 18 21 C10 20.5 3.5 14 3 6 C3 4 4.5 3 6 3 Z" fill="none" stroke="#fff" stroke-width="1.6"/><path d="M14 3 A7 7 0 0 1 21 10 M14 6.5 A3.5 3.5 0 0 1 17.5 10" fill="none" stroke="#fff" stroke-width="1.4"/></svg>
      <svg width="22" height="22" viewBox="0 0 24 24" aria-hidden="true"><circle cx="12" cy="12" r="10" fill="none" stroke="#fff" stroke-width="1.4"/><ellipse cx="12" cy="12" rx="4.5" ry="10" fill="none" stroke="#fff" stroke-width="1.2"/><path d="M2 12 H22 M4 7 H20 M4 17 H20" stroke="#fff" stroke-width="1.2"/></svg>
    </div>
    <p>0498765432</p>
    <p>www.brennaskincare.com</p>
  </div>
</section>

<section class="page page--back">
  <svg class="shapes" width="737" height="1040" viewBox="0 0 737 1040" aria-hidden="true">
    <path d="M0 268 C90 262 160 282 240 276 C330 270 360 248 440 246 C530 244 560 266 640 262 C690 259 720 250 737 246 L737 512 C660 526 600 520 520 524 C440 528 420 536 330 534 C240 532 180 526 100 530 C60 532 25 538 0 542 Z" fill="var(--navy)"/>
    <path d="M430 860 C480 850 520 868 590 860 C650 853 700 848 737 852 L737 1040 L430 1040 Z" fill="var(--navy)"/>
  </svg>

  <div class="divider divider--top"></div>
  <div class="divider divider--bottom"></div>

  <article class="product product--light col-left row-1">
    <h2 class="product__name">Hydrating Moisturiser</h2>
    <p class="product__meta">60ml | <span class="product__price">$18</span></p>
    <p class="product__skin">Normal/Dry/Mature Skin Types</p>
    <p class="product__key">Key Ingredients</p>
    <ul class="ingredients">
      <li><strong>Rosehip Oil</strong><span>Rich in essential fatty acids which are integral for skin regeneration and boosting collagen formation.</span></li>
      <li><strong>Green Tea Leaf Extract</strong><span>Anti-inflammatory benefits which reduce redness and soothes skin irritation.</span></li>
      <li><strong>Davidson Plum Extract</strong><span>Improves the appearance of fine lines and wrinkles and rich in antioxidants.</span></li>
    </ul>
  </article>

  <article class="product product--light col-right row-1">
    <h2 class="product__name">Balancing Moisturiser</h2>
    <p class="product__meta">60ml | <span class="product__price">$18</span></p>
    <p class="product__skin">Oily | Combination | Problematic Skin Types</p>
    <p class="product__key">Key Ingredients</p>
    <ul class="ingredients">
      <li><strong>Grape Seed Oil</strong><span>Acts as an anti-inflammatory and effective in combating acne.</span></li>
      <li><strong>Licorice Root Extract</strong><span>Provides skin brightening effects and soothes itchy and irritated skin.</span></li>
      <li><strong>Quandong (Sandalwood) Extract</strong><span>High in vitamin C, reduces the appearance of ageing such as dark circles and pigmentation.</span></li>
    </ul>
  </article>

  <article class="product product--dark col-left row-2">
    <h2 class="product__name">Eye Cream</h2>
    <p class="product__meta">15 ML | <span class="product__price">$19</span></p>
    <p class="product__skin">All Skin Types</p>
    <p class="product__key">Key Ingredients</p>
    <ul class="ingredients" style="margin-top:16px">
      <li><strong>Cucumis Sativus (Cucumber) Seed Oil</strong><span>Highly moisturising with Vitamin E, it balances the skin &amp; encourages healthy skin regeneration.</span></li>
      <li><strong>Kakadu Plum Extract</strong><span>Rich in Vitamin C &amp; Gallic acid which has anti-inflammatory properties, can help reduce pigmentation and dark spots.</span></li>
      <li><strong>Quandong Extract</strong><span>High in Rutin, an antioxidant that soothes skin and calms redness, it also reduces the signs of ageing.</span></li>
    </ul>
  </article>

  <article class="product product--dark col-right row-2">
    <h2 class="product__name">Facial Cleansing Gel</h2>
    <p class="product__meta">125ML | <span class="product__price">$20</span></p>
    <p class="product__skin">Oily | Combination | Problematic Skin Types</p>
    <p class="product__key">Key Ingredients</p>
    <ul class="ingredients" style="margin-top:16px">
      <li><strong>Vitamin E</strong><span>A natural antioxidant that helps to protect the face from exposure to the sun and increases skin elasticity. It also reduces acne, blemishes and soothes the skin.</span></li>
      <li><strong>Aloe Vera Juice</strong><span>Hydrates &amp; exfoliates the face, reducing inflammation, acne and dry skin.</span></li>
      <li><strong>Kakadu Plum Extract</strong><span>Rich in Vitamin C &amp; Gallic acid which has anti-inflammatory properties, can help reduce pigmentation and dark spots. Also stimulates growth of collagen.</span></li>
    </ul>
  </article>

  <article class="product product--light col-left row-3">
    <h2 class="product__name">Vitamin C Serum</h2>
    <p class="product__meta">30ML | <span class="product__price">$15</span></p>
    <p class="product__skin">All Skin types</p>
    <p class="product__key">Key Ingredients</p>
    <ul class="ingredients">
      <li><strong>Sodium Phytate</strong><span>Contains stabilising properties that moisturises the skin, helps reduce pore size and improve the appearance of cellulite.</span></li>
      <li><strong>Davidson Plum Extract</strong><span>Improves the appearance of fine lines and wrinkles and rich in antioxidants.</span></li>
      <li><strong>Vitamin C (Sodium Ascorbyl Phosphate)</strong><span>Contains anti-inflammatory and anti-ageing properties and helps fight acne and blemishes.</span></li>
    </ul>
  </article>

  <article class="product product--light col-right row-3">
    <h2 class="product__name">Perfecting Toning Mist</h2>
    <p class="product__meta">125ML | <span class="product__price">$17.50</span></p>
    <p class="product__skin">All Skin types</p>
    <p class="product__key">Key Ingredients</p>
    <ul class="ingredients">
      <li><strong>Rose Flower Water</strong><span>Contains anti-ageing properties, hydrates the skin and soothes skin irritation.</span></li>
      <li><strong>Green Tea Leaf Extract</strong><span>Anti-inflammatory benefits which reduce redness and soothes skin irritation.</span></li>
      <li><strong>Kakadu Plum</strong><span>Rich in Vitamin C &amp; Gallic acid which has anti-inflammatory properties, can help reduce pigmentation and dark spots. It also stimulates growth of collagen and reduces wrinkles.</span></li>
    </ul>
  </article>

  <article class="product product--light product--body col-left row-4">
    <h2 class="product__name">Body Balm</h2>
    <p class="product__meta">250ML | <span class="product__price">$18</span></p>
    <p class="product__skin">All skin types</p>
    <p class="product__key">Key Ingredients</p>
    <ul class="ingredients" style="margin-top:16px">
      <li><strong>Kakadu Plum Extract</strong><span>Rich in Vitamin C &amp; Gallic acid which has anti-inflammatory properties, can help reduce pigmentation and dark spots. Also stimulates growth of collagen.</span></li>
      <li><strong>Panthenol (Vitamin B5)</strong><span>An anti-inflammatory skin barrier repairer that improves the appearance of skin, preventing dryness and keeping the skin balanced.</span></li>
      <li><strong>Desert Lime Extract</strong><span>High in Vitamin C &amp; antioxidants, it vitalises the skin, keeping it nourished and rejuvenated.</span></li>
    </ul>
  </article>

  <div class="contact-card">
    <h3>Contact Us</h3>
    <p class="company">Brenna Skincare</p>
    <p class="line"><svg width="9" height="9" viewBox="0 0 24 24" aria-hidden="true"><path d="M6 3 L9 3 L10.5 8 L8.5 9.5 C9.5 12 12 14.5 14.5 15.5 L16 13.5 L21 15 L21 18 C21 19.5 20 21 18 21 C10 20.5 3.5 14 3 6 C3 4 4.5 3 6 3 Z" fill="#fff"/></svg>0498765432</p>
    <p class="line"><svg width="9" height="9" viewBox="0 0 24 24" aria-hidden="true"><circle cx="12" cy="12" r="10" fill="none" stroke="#fff" stroke-width="2.5"/><path d="M2 12 H22 M12 2 V22" stroke="#fff" stroke-width="2"/></svg>www.brennaskincare.com</p>
  </div>
</section>

</body>
</html>
```